Architecture firm needing a business card

We need a business card design for a new company based in the US called "Pellmore Architecture". Seeking minimalist designs that have a creativity/design feel but must be clean and professional. Please refer to the logo attached.

Target Market(s)

Real Estate Investors, Home Builders and Construction Firms.

Industry/Entity Type

Architecture

Contact Information for Business Card

Standard US size business cards. Would like to have some sort of graphic on the back side of the card - nothing that is too loud but something that may catch your attention. More or less grayscale colors that are in line with the logo colors (navy and greys essentially). Additional colors maybe accepted if blended properly (earthtones), but might be difficult to accomplish and maintain the clean/minimalist look.

Requirements
Must have
• Clean Lines
Nice to have
• some sort of graphics, would like to have something creative on the back side of the card
Should not have
• nothing too busy, cluttered or overwhelming.

```html
<!DOCTYPE html>
<html lang="en">
<head>
<meta charset="UTF-8">
<title>Pellmore Architecture – Business Card</title>
<link rel="stylesheet" href="https://fonts.googleapis.com/css2?family=Lato:wght@300;400;700&display=swap">
<style>
  :root{
    --navy:#1f4470;
    --navy-deep:#1a3b62;
    --grey:#9b9b9b;
    --rule:#d9d9d9;
    --paper:#ffffff;
    --stage:#2b2b2b;
    --ink-light:#ffffff;
  }
  *{box-sizing:border-box;margin:0;padding:0}
  html,body{width:1200px;height:750px;overflow:hidden;background:var(--stage);font-family:"Lato",Arial,sans-serif}
  .canvas{width:1200px;height:750px;display:flex;flex-direction:column;align-items:center;justify-content:center;gap:40px}
  .card{width:560px;height:320px;position:relative;overflow:hidden;box-shadow:0 10px 30px rgba(0,0,0,.45)}

  /* back side */
  .card-back{background:var(--navy);display:flex;flex-direction:column;align-items:center;justify-content:center;gap:34px}
  .back-brand{display:flex;align-items:center;gap:16px;color:var(--ink-light);font-weight:400;font-size:34px;letter-spacing:1px}
  .brand-square{width:30px;height:30px;border:3px solid currentColor}
  .back-web{color:var(--ink-light);font-size:11px;letter-spacing:5px;font-weight:300}

  /* front side */
  .card-front{background:var(--paper)}
  .front-top{position:absolute;left:0;top:0;width:100%;height:168px;display:flex;align-items:center;justify-content:center}
  .front-brand{display:flex;align-items:center;gap:12px;color:var(--navy);font-weight:400;font-size:30px;letter-spacing:1px}
  .front-brand .brand-square{width:24px;height:24px}
  .front-rule{position:absolute;left:0;top:168px;width:100%;height:5px;background:var(--rule)}
  .front-bottom{position:absolute;left:0;top:173px;width:100%;height:147px;background:var(--navy);color:var(--ink-light);display:flex;align-items:center;justify-content:center}
  .person{text-align:right;padding-right:20px;border-right:1px solid rgba(255,255,255,.55)}
  .person-name{font-weight:700;font-size:17px}
  .person-title{font-size:12px;margin-bottom:8px}
  .person-address{font-size:11px;line-height:1.45}
  .contacts{list-style:none;padding-left:20px;font-size:11.5px;line-height:1.75}
  .contacts li{display:flex;align-items:center;gap:8px}
  .contacts svg{width:12px;height:12px;fill:var(--ink-light)}
</style>
</head>
<body>
<main class="canvas">
  <section class="card card-back">
    <div class="back-brand"><span class="brand-square"></span>Pellmore Architecture</div>
    <div class="back-web">www.pellmorearch.com</div>
  </section>

  <section class="card card-front">
    <div class="front-top">
      <div class="front-brand"><span class="brand-square"></span>Pellmore Architecture</div>
    </div>
    <div class="front-rule"></div>
    <div class="front-bottom">
      <div class="person">
        <div class="person-name">Daniel Reyes</div>
        <div class="person-title">President</div>
        <div class="person-address">4127 Harwell Avenue<br>Cedar Hollow, NY 11020</div>
      </div>
      <ul class="contacts">
        <li><svg viewBox="0 0 12 12"><path d="M1 4c0-2 2-3 5-3s5 1 5 3l-2 1-1-1.5H4L3 5zM2 6h8l1 5H1z"/></svg>555 0142 7781</li>
        <li><svg viewBox="0 0 12 12"><path d="M3 0h6v12H3zM4 1.5v8h4v-8z"/></svg>555 0198 3364</li>
        <li><svg viewBox="0 0 12 12"><path d="M3 0h6v4H3zM0 4h12v6H9v2H3v-2H0zM4 8v3h4V8z"/></svg>555 0167 4420</li>
        <li><svg viewBox="0 0 12 12"><path d="M0 2h12v8H0zM1 3l5 4 5-4v-.2H1z" fill-rule="evenodd"/></svg>daniel@pellmorearch.com</li>
      </ul>
    </div>
  </section>
</main>
</body>
</html>
```